KRV Business Cards

We are a local commercial development company based in Silicon Valley and we would like a new business card. I've attached a copy of our company brochure to give a flavor of what we do, our logo, info company colors/graphics, and our current business card. We don't necessarily need a crazy makeover, but would like something that feels a little bit more "fresh" and modern (we've had the same business card design for 15+ years), but still in keeping with our overall brand -- clean, high-quality, modern but timeless. Would like to add our website to the info on the card (www.velmara.com) and would like the flexibility for some folks to have an efax number listed and some not to have that included (without it looking like there is a hole).

```html
<!DOCTYPE html>
<html lang="en">
<head>
<meta charset="utf-8">
<title>KRV Business Cards</title>
<link rel="stylesheet" href="https://fonts.googleapis.com/css2?family=Source+Sans+3:wght@400;600;700&display=swap">
<style>
  :root {
    --backdrop: #2b2d30;
    --paper: #fbfbfa;
    --navy: #2f4a68;
    --ink: #3d3f42;
    --title-blue: #5b80a8;
    --muted: #6b6d70;
  }
  * { box-sizing: border-box; margin: 0; padding: 0; }
  html, body {
    width: 1200px; height: 900px; overflow: hidden;
    background: var(--backdrop);
    font-family: "Source Sans 3", Arial, sans-serif;
  }
  .card {
    position: absolute; left: 240px;
    width: 720px; height: 410px;
    background: var(--paper);
    box-shadow: 0 8px 24px rgba(0,0,0,0.45);
  }
  .card--front { top: 30px; }
  .card--back { top: 462px; }

  .brand {
    position: absolute;
    display: flex; align-items: center; gap: 18px;
    color: var(--navy);
  }
  .brand__square { width: 22px; height: 22px; background: var(--navy); flex: none; }
  .brand__name {
    font-weight: 600; text-transform: uppercase;
    letter-spacing: 0.08em; line-height: 1.15;
  }
  .card--front .brand { left: 200px; top: 112px; }
  .card--front .brand__name { font-size: 34px; }
  .card--back .brand { left: 400px; top: 44px; }
  .card--back .brand__name { font-size: 25px; }

  .website {
    position: absolute; left: 0; right: 0; top: 318px;
    text-align: center;
    font-size: 15px; letter-spacing: 0.5em;
    color: var(--muted);
  }

  .rule { position: absolute; background: var(--navy); }
  .rule--top { left: 40px; right: 40px; top: 178px; height: 2px; }
  .rule--bottom { left: 40px; right: 240px; top: 296px; height: 1.5px; }

  .person { position: absolute; left: 40px; top: 224px; }
  .person__name { font-size: 27px; font-weight: 700; color: var(--navy); line-height: 1.2; }
  .person__title { font-size: 17px; color: var(--title-blue); margin-top: 2px; }

  .contact {
    position: absolute; left: 40px; right: 40px; top: 310px;
    font-size: 17px; color: var(--ink); line-height: 1.5;
  }
  .contact__label { font-weight: 700; color: var(--navy); }
  .contact__line span + span { margin-left: 6px; }
</style>
</head>
<body>
  <section class="card card--front">
    <div class="brand">
      <div class="brand__square"></div>
      <div class="brand__name">KRV<br>Development<br>Company, LLC</div>
    </div>
    <p class="website">www.velmara.com</p>
  </section>

  <section class="card card--back">
    <div class="brand">
      <div class="brand__square"></div>
      <div class="brand__name">KRV<br>Development<br>Company, LLC</div>
    </div>
    <div class="rule rule--top"></div>
    <div class="person">
      <h1 class="person__name">Jana L. Whitcombe</h1>
      <p class="person__title">Partner</p>
    </div>
    <div class="rule rule--bottom"></div>
    <div class="contact">
      <p>212 Orchard Lane Brenton Falls, Vermont 05099</p>
      <p class="contact__line">
        <span><b class="contact__label">P:</b> 650.555.0142</span>
        <span><b class="contact__label">M:</b> 650.555.0187</span>
        <span><b class="contact__label">F:</b> 650.555.0163</span>
        <span><b class="contact__label">E:</b> jana@velmara.com</span>
      </p>
    </div>
  </section>
</body>
</html>
```